A Small Coastal town of New Zealand book!

we want a cool book cover for our book titled; Karewa Bay & The Wild Western Coasts - Old Tales, Boating, Hiking and sights to see...

attached are some screenshots of books we found that were similar to the topic i cover.

also attached are some screenshots of some ideas i have been playing with my self with myself on canva...

i quite like the first one how he managed to put 5 images there without making it look too busy...

Target Market(s)

Tourists

Industry/Entity Type

Tourism

Font styles to use
Serif
Sans Serif

Requirements
Must have
• Nice coastal image and good fonts and text placement
Should not have
• not to busy...

```html
<!DOCTYPE html>
<html lang="en">
<head>
<meta charset="utf-8">
<title>Karewa Bay &amp; The Wild Western Coasts – Book Cover</title>
<link rel="stylesheet" href="https://fonts.googleapis.com/css2?family=Tinos:ital,wght@0,400;0,700;1,400;1,700&display=swap">
<style>
  :root {
    --stage: #dfe4e8;
    --sky-top: #5aa2de;
    --sky-mid: #8cc2ec;
    --sea: #1f6fc0;
    --land: #8aa63e;
    --land-dark: #4f7a30;
    --panel: #1d3e58;
    --panel-band: #172f44;
    --ink: #1b2430;
    --white: #ffffff;
    --badge: #4a80e2;
    --frame: #1f3f5c;
  }
  * { margin: 0; padding: 0; box-sizing: border-box; }
  html, body { width: 1200px; height: 1200px; overflow: hidden; background: var(--stage); }
  body { position: relative; font-family: "Tinos", "Times New Roman", serif; }

  .cover {
    position: absolute; left: 0; top: 170px; width: 1200px; height: 865px; overflow: hidden;
  }
  .cover-photo {
    position: absolute; inset: 0;
    background: linear-gradient(180deg,
      var(--sky-top) 0%, var(--sky-mid) 38%, #b9d9f0 48%,
      var(--sea) 55%, #2a86c8 62%, var(--land) 70%, var(--land-dark) 88%, #6f8f3a 100%);
  }

  .back-copy {
    position: absolute; left: 66px; top: 75px; width: 446px;
    font-size: 14.6px; line-height: 18.7px; color: var(--ink); text-align: justify;
  }
  .back-copy p + p { margin-top: 18.7px; }
  .back-copy .lead { font-weight: 700; font-style: italic; }

  .spine-title {
    position: absolute; left: 627px; top: 146px; transform-origin: 0 0; transform: rotate(90deg);
    color: var(--ink); white-space: nowrap; line-height: 21px;
  }
  .spine-title .main { font-size: 20px; display: block; }
  .spine-title .sub { font-size: 19px; font-style: italic; display: block; }

  .spine-url {
    position: absolute; left: 614px; top: 688px; transform-origin: 0 0; transform: rotate(90deg);
    font-size: 15px; font-style: italic; color: var(--ink); white-space: nowrap;
  }

  .title-panel {
    position: absolute; left: 628px; top: 146px; width: 572px; height: 292px; background: var(--panel); color: var(--white);
  }
  .title-main { position: absolute; left: 78px; top: 44px; font-size: 70px; line-height: 1; letter-spacing: -1px; }
  .title-second { position: absolute; left: 78px; top: 120px; display: flex; align-items: center; gap: 14px; }
  .title-second .word { font-size: 70px; line-height: 1; letter-spacing: -1px; }
  .title-second .tag { font-size: 26px; font-style: italic; line-height: 27px; }
  .title-band {
    position: absolute; left: 0; bottom: 0; width: 100%; height: 78px; background: var(--panel-band);
    display: flex; align-items: center; justify-content: center; font-size: 20px;
  }

  .thumb {
    position: absolute; border: 6px solid var(--frame);
    background: linear-gradient(180deg, #9ccaf0 0%, #3d93d3 45%, #86a851 75%, #5e8a3a 100%);
  }
  .thumb-1 { left: -20px; top: 570px; width: 210px; height: 115px; transform: rotate(-4deg); }
  .thumb-2 { left: -20px; top: 685px; width: 190px; height: 100px; transform: rotate(-3deg);
    background: linear-gradient(180deg, #cfe4f5 0%, #a9cdee 60%, #6fb0e2 100%); }
  .thumb-3 { left: -20px; top: 790px; width: 225px; height: 100px; transform: rotate(-2deg); }

  .map-badge {
    position: absolute; left: 659px; top: 710px; width: 130px; height: 130px; border-radius: 50%;
    background: var(--badge); color: var(--white); text-align: center;
    display: flex; flex-direction: column; justify-content: center; line-height: 29px;
  }
  .map-badge .free { font-size: 26px; }
  .map-badge .handy { font-size: 28px; font-weight: 700; }
  .map-badge .map { font-size: 26px; }

  .front-url {
    position: absolute; right: 28px; top: 816px; font-size: 21px; font-style: italic; color: var(--white);
  }
  .front-url b { font-weight: 700; }
</style>
</head>
<body>
  <main class="cover">
    <div class="cover-photo" role="img" aria-label="Aerial photograph of a coastal bay with a river mouth, sandy beaches, green hills and open sea under a blue sky"></div>

    <section class="back-copy">
      <p><span class="lead">Lorem ipsum dolor sit amet,</span> consectetur adipiscing elit, sed do eiusmod tempor incididunt ut labore et dolore magna aliqua. In hac habitasse platea dictumst quisque sagittis purus sit. Turpis egestas maecenas pharetra convallis posuere morbi leo urna. Ultrices eros in cursus turpis massa tincidunt. Interdum varius sit amet mattis vulputate enim nulla aliquet.</p>
      <p>At volutpat diam ut venenatis tellus. Cursus mattis molestie a iaculis at erat pellentesque adipiscing commodo. Mattis molestie a iaculis at erat pellentesque adipiscing. Leo vel orci porta non pulvinar neque laoreet. Vulputate ut pharetra sit amet aliquam.</p>
      <p>Viverra tellus in hac habitasse platea dictumst vestibulum rhoncus. Velit aliquet sagittis id consectetur purus ut faucibus. Purus semper eget duis at tellus. Elementum facilisis leo vel fringilla est. Molestie ac feugiat sed lectus. Ut diam quam nulla porttitor. Ut sem nulla pharetra diam. Sapien nec sagittis aliquam malesuada bibendum arcu vitae.</p>
    </section>

    <div class="thumb thumb-1" role="img" aria-label="Photo of turquoise coastline and rocky islets"></div>
    <div class="thumb thumb-2" role="img" aria-label="Photo of sky over the sea horizon"></div>
    <div class="thumb thumb-3" role="img" aria-label="Photo of the bay and beach from above"></div>

    <div class="spine-title">
      <span class="main">KAREWA BAY</span>
      <span class="sub">&amp; The Wild Western Coasts</span>
    </div>
    <div class="spine-url">www.<b>karewabay</b>.co.nz</div>

    <header class="title-panel">
      <h1 class="title-main">KAREWA BAY</h1>
      <div class="title-second">
        <span class="word">&amp; THE</span>
        <span class="tag">The Wild<br>Western Coasts</span>
      </div>
      <p class="title-band">Old Tales, Boating, Hiking and sights to see...</p>
    </header>

    <div class="map-badge">
      <span class="free">Free</span>
      <span class="handy">Handy</span>
      <span class="map">Map</span>
    </div>

    <p class="front-url">www.<b>karewabay</b>.co.nz</p>
  </main>
</body>
</html>
```